Wow me with your Earring card options!

An A7 portrait sized earring card is required for Velvet & Vinyl. Inspired by Velvet and fueled by Vinyl we love our accessories to do the talking. Bold statement earrings are our thing. Our earring cards need to showcase our brand while not stealing all of the limelight from the earrings themselves. Earring care information needs to be included on the back side of the card. Our simple logo needs to be the basis for the colour choices used on the card.

Need extra days to review

• No florals please 😊

```html
<!DOCTYPE html>
<html lang="en">
<head>
<meta charset="utf-8">
<title>Velvet &amp; Vinyl — Earring Card</title>
<link href="https://fonts.googleapis.com/css2?family=Montserrat:wght@400;500;600&family=Allura&display=swap" rel="stylesheet">
<style>
  :root{
    --bg:#3a3a3c;
    --ink:#3b3b3b;
    --black:#070707;
    --white:#ffffff;
    --teal:#0e9aa0;
    --green:#77d04e;
    --yellow:#ffd94a;
    --orange:#ff7a1a;
    --pink:#ff3aa6;
    --purple:#6a2ae8;
    --rule:#b9b9b9;
  }
  *{box-sizing:border-box;margin:0;padding:0}
  html,body{width:1200px;height:1200px;overflow:hidden;background:var(--bg)}
  .canvas{position:relative;width:1200px;height:1200px;display:flex;gap:60px;justify-content:center;align-items:center}
  .card{position:relative;width:480px;height:680px;flex:none}
  .card--front{background:var(--black)}
  .card--back{background:var(--white)}
  .frame{position:absolute;inset:0;width:100%;height:100%}
  .brand{position:absolute;inset:0;display:flex;flex-direction:column;justify-content:center;align-items:center;
    font-family:'Montserrat',sans-serif;font-weight:600;color:var(--white);font-size:64px;line-height:1.05;letter-spacing:1px;text-align:center}
  .back-content{position:absolute;inset:60px 56px 50px;display:flex;flex-direction:column;align-items:center;font-family:'Montserrat',sans-serif;color:var(--ink)}
  .title{font-weight:600;font-size:66px;letter-spacing:1px;line-height:1}
  .title .c1{color:var(--teal)}.title .c2{color:var(--green)}.title .c3{color:var(--yellow)}
  .title .c4{color:var(--orange)}.title .c5{color:var(--pink)}.title .c6{color:var(--purple)}.title .c7{color:var(--ink)}
  .subtitle{font-family:'Allura',cursive;font-size:50px;line-height:1;margin-top:2px;margin-left:40px}
  .care-list{list-style:none;width:100%;margin-top:24px}
  .care-item{display:flex;align-items:center;gap:26px;padding:14px 0 14px 10px;border-top:1px solid var(--rule);font-size:17px;line-height:1.3}
  .care-item:first-child{border-top:none}
  .care-icon{width:56px;height:48px;flex:none;stroke:var(--teal);fill:none;stroke-width:2.4;stroke-linecap:round;stroke-linejoin:round}
  .contact{margin-top:auto;width:100%;padding-left:70px;font-size:15px;line-height:1.6}
  .contact-row{display:flex;align-items:center;gap:8px}
  .contact-row svg{width:14px;height:14px;fill:var(--teal)}
  .follow{display:flex;align-items:center;gap:14px;margin-top:6px}
  .follow-label{color:var(--teal);font-size:15px}
  .social{display:flex;gap:10px}
  .social span{display:block;width:32px;height:32px;border-radius:50%;background:var(--teal)}
</style>
</head>
<body>
<main class="canvas">

  <section class="card card--front" aria-label="Card front">
    <svg class="frame" viewBox="0 0 480 680" aria-hidden="true">
      <defs>
        <linearGradient id="sideL" x1="0" y1="0" x2="0" y2="1">
          <stop offset="0" stop-color="#0e9aa0"/><stop offset=".22" stop-color="#0e9aa0"/>
          <stop offset=".22" stop-color="#77d04e"/><stop offset=".44" stop-color="#77d04e"/>
          <stop offset=".44" stop-color="#ffd94a"/><stop offset=".66" stop-color="#ffd94a"/>
          <stop offset=".66" stop-color="#ff3aa6"/><stop offset=".84" stop-color="#ff3aa6"/>
          <stop offset=".84" stop-color="#6a2ae8"/><stop offset="1" stop-color="#6a2ae8"/>
        </linearGradient>
        <linearGradient id="sideR" x1="0" y1="0" x2="0" y2="1">
          <stop offset="0" stop-color="#0e9aa0"/><stop offset=".12" stop-color="#0e9aa0"/>
          <stop offset=".12" stop-color="#77d04e"/><stop offset=".3" stop-color="#77d04e"/>
          <stop offset=".3" stop-color="#ffd94a"/><stop offset=".5" stop-color="#ffd94a"/>
          <stop offset=".5" stop-color="#ff3aa6"/><stop offset=".72" stop-color="#ff3aa6"/>
          <stop offset=".72" stop-color="#6a2ae8"/><stop offset="1" stop-color="#6a2ae8"/>
        </linearGradient>
      </defs>
      <rect x="22" y="22" width="436" height="7" fill="#0e9aa0"/>
      <rect x="22" y="651" width="436" height="7" fill="#6a2ae8"/>
      <rect x="22" y="22" width="7" height="636" fill="url(#sideL)"/>
      <rect x="451" y="22" width="7" height="636" fill="url(#sideR)"/>
    </svg>
    <h1 class="brand">Velvet<br>&amp; Vinyl</h1>
  </section>

  <section class="card card--back" aria-label="Card back">
    <svg class="frame" viewBox="0 0 480 680" aria-hidden="true">
      <rect x="22" y="22" width="436" height="7" fill="#0e9aa0"/>
      <rect x="22" y="651" width="436" height="7" fill="#6a2ae8"/>
      <rect x="22" y="22" width="7" height="636" fill="url(#sideL)"/>
      <rect x="451" y="22" width="7" height="636" fill="url(#sideR)"/>
    </svg>
    <div class="back-content">
      <h2 class="title"><span class="c1">E</span><span class="c2">A</span><span class="c3">R</span><span class="c4">R</span><span class="c5">I</span><span class="c6">N</span><span class="c7">G</span></h2>
      <p class="subtitle">Care Instruction</p>
      <ul class="care-list">
        <li class="care-item">
          <svg class="care-icon" viewBox="0 0 56 48"><path d="M22 10c-6 9-10 14-10 20a10 10 0 0 0 20 0c0-6-4-11-10-20z"/><path d="M38 6c-3 5-5 7-5 10a5 5 0 0 0 10 0c0-3-2-5-5-10z"/><path d="M17 31a5 5 0 0 0 5 5"/></svg>
          <span>Avoid moisture<br>&amp; remove before bathing</span>
        </li>
        <li class="care-item">
          <svg class="care-icon" viewBox="0 0 56 48"><rect x="6" y="22" width="44" height="12" rx="2"/><path d="M10 22V10h36v12"/><rect x="14" y="15" width="11" height="7" rx="2"/><rect x="31" y="15" width="11" height="7" rx="2"/><path d="M10 34v6M46 34v6"/></svg>
          <span>For comforts sake,<br>remove before bed!</span>
        </li>
        <li class="care-item">
          <svg class="care-icon" viewBox="0 0 56 48"><rect x="20" y="18" width="16" height="26" rx="3"/><rect x="23" y="10" width="10" height="8"/><path d="M38 8h2M42 5h2M42 11h2M46 8h2"/></svg>
          <span>Avoid contact with<br>perfumes &amp; lotions</span>
        </li>
        <li class="care-item">
          <svg class="care-icon" viewBox="0 0 56 48"><circle cx="28" cy="24" r="11"/><path d="M22 27a7 7 0 0 0 12 0"/><path d="M28 4v5M28 39v5M8 24h5M43 24h5M14 10l4 4M38 34l4 4M42 10l-4 4M18 34l-4 4"/></svg>
          <span>Store away from<br>direct sunlight</span>
        </li>
      </ul>
      <div class="contact">
        <p class="contact-row"><svg viewBox="0 0 14 14"><path d="M1 3h12v8H1z M1 3l6 5 6-5" /></svg>hello@velvetandvinyl.com.au</p>
        <p class="contact-row"><svg viewBox="0 0 14 14"><circle cx="7" cy="7" r="6"/></svg>www.velvetandvinyl.com.au</p>
        <div class="follow">
          <span class="follow-label">FOLLOW US ON</span>
          <span>@velvetandvinyl</span>
        </div>
        <div class="social" role="img" aria-label="Social media links">
          <span></span><span></span><span></span><span></span>
        </div>
      </div>
    </div>
  </section>

</main>
</body>
</html>
```